Harlow Grading LLC business card design

Excavation company business cards

Contact Information for Business Card

Harlow Grading LLC cell phone 208-471-9360 office phone 208-396-4815 harlowgradingllc@mailverde.net Driveways, site prep, retaining walls, septic systems, rock delivery

Colors

Designer to choose colors to be used in the design.

```html
<!DOCTYPE html>
<html lang="en">
<head>
<meta charset="utf-8">
<title>Harlow Grading LLC — Business Card</title>
<link rel="stylesheet" href="https://fonts.googleapis.com/css2?family=Montserrat:wght@500;600;700&display=swap">
<style>
  :root {
    --backdrop: #d4d4d4;
    --card: #0c0c0c;
    --pattern-dark: #0e0e0e;
    --pattern-light: #2c2c2c;
    --orange: #e06a1b;
    --white: #f2f2f2;
    --stripe: #8a8a8a;
  }
  * { box-sizing: border-box; margin: 0; padding: 0; }
  html, body { width: 1084px; height: 1200px; overflow: hidden; }
  body {
    background: var(--backdrop);
    font-family: "Montserrat", sans-serif;
    position: relative;
  }
  .card {
    position: absolute;
    left: 102px;
    width: 880px;
    height: 506px;
    background: var(--card);
    box-shadow: 0 6px 14px rgba(0,0,0,0.35);
    overflow: hidden;
  }
  .card--front { top: 64px; }
  .card--back { top: 630px; }

  /* Front */
  .front-pattern {
    position: absolute; inset: 0;
    background: linear-gradient(90deg, var(--pattern-dark) 0%, #151515 45%, var(--pattern-light) 100%);
  }
  .brand-name {
    position: absolute;
    color: var(--orange);
    font-weight: 700;
    letter-spacing: 1px;
    line-height: 1.05;
    text-align: center;
    text-transform: uppercase;
  }
  .front-brand {
    left: 330px; top: 200px; width: 220px;
    font-size: 30px;
  }
  .services {
    position: absolute;
    left: 50px; right: 50px; top: 408px;
    color: var(--white);
    font-size: 17px;
    font-weight: 500;
    text-transform: uppercase;
    white-space: nowrap;
  }
  .services .dot {
    display: inline-block;
    width: 6px; height: 6px;
    border-radius: 50%;
    background: var(--orange);
    margin: 0 8px 3px;
    vertical-align: middle;
  }

  /* Back */
  .back-brand {
    left: 600px; top: 75px; width: 225px;
    font-size: 30px;
  }
  .person {
    position: absolute;
    right: 500px; top: 232px;
    text-align: right;
  }
  .person__name {
    color: var(--orange);
    font-size: 34px;
    font-weight: 600;
    text-transform: uppercase;
    line-height: 1.1;
  }
  .person__title {
    color: var(--white);
    font-size: 22px;
    font-weight: 500;
  }
  .divider {
    position: absolute;
    left: 399px; top: 234px;
    width: 2px; height: 76px;
    background: var(--white);
  }
  .contacts {
    position: absolute;
    left: 420px; top: 232px;
    list-style: none;
    color: var(--white);
    font-size: 20px;
    font-weight: 500;
  }
  .contacts li {
    display: flex; align-items: center;
    height: 28px;
  }
  .contacts svg { width: 14px; height: 14px; margin-right: 16px; fill: var(--orange); }
  .web-band {
    position: absolute;
    left: 0; right: 0; bottom: 0;
    height: 34px;
  }
  .web-band svg { position: absolute; inset: 0; }
  .web-band__url {
    position: absolute; inset: 0;
    display: flex; align-items: center; justify-content: center;
    color: var(--white);
    font-size: 20px;
    font-weight: 500;
  }
</style>
</head>
<body>

  <section class="card card--front">
    <div class="front-pattern" role="img" aria-label="Repeating faint pattern of excavator and mountain marks across the card"></div>
    <div class="brand-name front-brand">Harlow Grading LLC</div>
    <p class="services">
      Driveways<span class="dot"></span>Site Prep<span class="dot"></span>Retaining Walls<span class="dot"></span>Septic Systems<span class="dot"></span>Rock Delivery
    </p>
  </section>

  <section class="card card--back">
    <div class="brand-name back-brand">Harlow Grading LLC</div>

    <div class="person">
      <p class="person__name">Wade Tolliver</p>
      <p class="person__title">President</p>
    </div>
    <div class="divider"></div>

    <ul class="contacts">
      <li>
        <svg viewBox="0 0 24 24" aria-hidden="true"><path d="M6.6 10.8a15.1 15.1 0 0 0 6.6 6.6l2.2-2.2c.3-.3.7-.4 1-.2 1.1.4 2.3.6 3.6.6.6 0 1 .4 1 1V20c0 .6-.4 1-1 1A17 17 0 0 1 3 4c0-.6.4-1 1-1h3.5c.6 0 1 .4 1 1 0 1.3.2 2.5.6 3.6.1.3 0 .7-.2 1z"/></svg>
        208-471-9360
      </li>
      <li>
        <svg viewBox="0 0 24 24" aria-hidden="true"><path d="M6.6 10.8a15.1 15.1 0 0 0 6.6 6.6l2.2-2.2c.3-.3.7-.4 1-.2 1.1.4 2.3.6 3.6.6.6 0 1 .4 1 1V20c0 .6-.4 1-1 1A17 17 0 0 1 3 4c0-.6.4-1 1-1h3.5c.6 0 1 .4 1 1 0 1.3.2 2.5.6 3.6.1.3 0 .7-.2 1z"/></svg>
        208-396-4815
      </li>
      <li>
        <svg viewBox="0 0 24 24" aria-hidden="true"><path d="M2 5h20v14H2z M3.5 6.5 12 13l8.5-6.5" fill="none" stroke="#e06a1b" stroke-width="2.4"/></svg>
        harlowgradingllc@mailverde.net
      </li>
    </ul>

    <div class="web-band">
      <svg viewBox="0 0 880 34" preserveAspectRatio="none" aria-hidden="true">
        <polygon points="18,0 34,0 16,34 0,34" fill="var(--stripe)"/>
        <polygon points="46,0 62,0 44,34 28,34" fill="var(--stripe)"/>
        <polygon points="74,0 90,0 72,34 56,34" fill="var(--stripe)"/>
        <polygon points="122,0 790,0 772,34 104,34" fill="var(--orange)"/>
        <polygon points="818,0 834,0 816,34 800,34" fill="var(--stripe)"/>
        <polygon points="846,0 862,0 844,34 828,34" fill="var(--stripe)"/>
        <polygon points="874,0 890,0 872,34 856,34" fill="var(--stripe)"/>
      </svg>
      <span class="web-band__url">www.HarlowGradingllc.net</span>
    </div>
  </section>

</body>
</html>
```